Quellan and Dermal Fillers

We need a poster designed to display outside our dental practice to advertise that we offer quellan and dermal fillers

Industry/Entity Type

Dental

```html
<!DOCTYPE html>
<html lang="en">
<head>
<meta charset="utf-8">
<title>We Offer Quellan &amp; Derma Fillers</title>
<link rel="stylesheet" href="https://fonts.googleapis.com/css2?family=Marcellus&family=Great+Vibes&display=swap">
<style>
  :root {
    --magenta-light: #b0247c;
    --magenta: #8c1262;
    --plum: #5a0a3e;
    --plum-deep: #300620;
    --petal-pink: #e04a9c;
    --petal-pale: #f6c2e0;
    --text-white: #ffffff;
    --amp-pink: #e879b8;
  }
  html, body {
    margin: 0;
    padding: 0;
    width: 849px;
    height: 1200px;
    overflow: hidden;
    background: var(--plum-deep);
  }
  .poster {
    position: relative;
    width: 849px;
    height: 1200px;
    overflow: hidden;
    background:
      radial-gradient(ellipse 520px 420px at 20% 18%, rgba(214, 70, 160, 0.55), transparent 70%),
      linear-gradient(180deg, var(--magenta-light) 0%, var(--magenta) 35%, var(--plum) 70%, var(--plum-deep) 100%);
  }
  .flower-art {
    position: absolute;
    left: 0;
    top: 560px;
    width: 849px;
    height: 640px;
    background:
      radial-gradient(ellipse 300px 230px at 46% 40%, rgba(246, 194, 224, 0.75), rgba(224, 74, 156, 0.45) 45%, transparent 75%),
      radial-gradient(ellipse 180px 150px at 8% 52%, rgba(240, 150, 200, 0.6), rgba(200, 50, 130, 0.3) 55%, transparent 80%),
      radial-gradient(ellipse 260px 200px at 70% 70%, rgba(224, 74, 156, 0.35), transparent 75%);
  }
  .headline {
    position: absolute;
    left: 408px;
    top: 70px;
    margin: 0;
    font-family: "Marcellus", "Times New Roman", serif;
    font-weight: 400;
    font-size: 78px;
    line-height: 76px;
    letter-spacing: 4px;
    color: var(--text-white);
  }
  .headline .line {
    display: block;
    position: relative;
  }
  .headline .line-gap {
    margin-top: 10px;
  }
  .ampersand {
    position: absolute;
    left: 232px;
    top: 212px;
    font-family: "Great Vibes", cursive;
    font-size: 72px;
    line-height: 1;
    color: var(--amp-pink);
    letter-spacing: 0;
  }
</style>
</head>
<body>
  <main class="poster">
    <div class="flower-art" role="img" aria-label="Translucent pink and white flower blossoms on slender stems"></div>
    <h1 class="headline">
      <span class="line">WE</span>
      <span class="line">OFFER</span>
      <span class="line">QUELLAN</span>
      <span class="ampersand" aria-hidden="true">&amp;</span>
      <span class="line line-gap">DERMA</span>
      <span class="line">FILLERS</span>
    </h1>
  </main>
</body>
</html>
```